Disc Golf Poster

Disc (NOT BALL GOLF) golf fundraiser for animal rescue (Tossin' for Tails on Cinco De Mayo) I want a poster similar to the one I have attached. This is a cinco de mayo themed event and the information is as follows:

Tossin' for Tails on Cinco De Mayo
Disc Golf Tournament

Two Rounds: First round singles for cash prize, followed by best-to-worst doubles for cash prize.

$30 Entry
$15 Payout
$15 Wag Haven Shelter

Wag Haven Shelter is a community outreach program and animal rescue. We offer free and low cost spay/neuter, flea/tick meds, food, treats, toys, collars and leashes to low income and homeless families in the North San Juan area. WHS also rescues senior and disabled animals from across the globe, WHS offer a hospice care to many of the animals. You can find more information on our website: www.waghaven-example.org

RAFFLE: We will have a donation bin set up at the event to collect new and gently used leashes, collars, dog beds, puppy pads, male wraps, toys, jackets, towels, blankets, brio laundry detergent and Vexol wipes, for every items donated you will receive one raffle ticket.

Cinco De Mayo themed lunch provided

May 5th, 2018 Check in at 9 am

Hollis Green 317 Marlow Street
Grass Valley, Ca

```html
<!DOCTYPE html>
<html lang="en">
<head>
<meta charset="utf-8">
<title>Tossin' for Tails on Cinco De Mayo – Disc Golf Tournament</title>
<link rel="stylesheet" href="https://fonts.googleapis.com/css2?family=Fredoka:wght@400;500;600;700&display=swap">
<style>
  :root {
    --olive: #9d9c2f;
    --olive-light: #a8a83a;
    --night: #141414;
    --sky: #a9d3ef;
    --cloud: #f4f6f2;
    --meadow: #8a9a2c;
    --meadow-pale: #c9cf7a;
    --white: #ffffff;
    --ink: #111111;
    --gold: #ffef16;
  }
  html, body {
    margin: 0;
    padding: 0;
    overflow: hidden;
    background: var(--olive);
  }
  .poster {
    position: relative;
    width: 868px;
    height: 1200px;
    overflow: hidden;
    background: linear-gradient(180deg, var(--olive) 0%, var(--olive-light) 100%);
    font-family: "Fredoka", sans-serif;
  }
  .hero-art {
    position: absolute;
    left: 0;
    top: 0;
    width: 868px;
    height: 620px;
    background:
      linear-gradient(180deg, rgba(20,20,20,0) 58%, rgba(20,20,20,0.5) 68%, rgba(157,156,47,0.6) 86%, var(--olive) 100%),
      radial-gradient(ellipse 170px 260px at 50% 42%, rgba(244,246,242,0.55) 0%, rgba(40,40,40,0.35) 70%, rgba(40,40,40,0) 100%),
      linear-gradient(90deg, var(--night) 0%, var(--night) 5%, rgba(20,20,20,0.35) 18%, rgba(20,20,20,0.05) 30%, rgba(20,20,20,0.05) 70%, rgba(20,20,20,0.35) 82%, var(--night) 95%, var(--night) 100%),
      linear-gradient(180deg, var(--night) 0%, var(--sky) 3%, var(--sky) 8%, var(--cloud) 14%, var(--cloud) 24%, var(--meadow-pale) 32%, var(--meadow) 44%, var(--meadow) 100%);
  }
  .event-title {
    position: absolute;
    left: 0;
    width: 868px;
    top: 490px;
    margin: 0;
    text-align: center;
    font-weight: 500;
    font-size: 41px;
    line-height: 51px;
    letter-spacing: 1px;
    color: var(--ink);
    text-shadow:
      0 0 4px var(--white), 3px 0 0 var(--white), -3px 0 0 var(--white),
      0 3px 0 var(--white), 0 -3px 0 var(--white), 3px 3px 0 var(--white),
      -3px -3px 0 var(--white), 3px -3px 0 var(--white), -3px 3px 0 var(--white),
      6px 0 2px var(--white), -6px 0 2px var(--white), 0 6px 2px var(--white), 0 -6px 2px var(--white);
  }
  .format {
    position: absolute;
    left: 0;
    width: 868px;
    top: 615px;
    margin: 0;
    text-align: center;
    color: var(--white);
    font-weight: 400;
    font-size: 29px;
    line-height: 37px;
    letter-spacing: 2px;
  }
  .price {
    position: absolute;
    top: 720px;
    margin: 0;
    text-align: center;
    color: var(--gold);
    font-weight: 700;
    font-size: 42px;
    line-height: 52px;
    -webkit-text-stroke: 2px var(--ink);
    paint-order: stroke fill;
    text-shadow: 0 0 3px var(--ink), 2px 2px 0 var(--ink), -2px -2px 0 var(--ink), 2px -2px 0 var(--ink), -2px 2px 0 var(--ink);
    transform: translateX(-50%);
    white-space: nowrap;
  }
  .price--entry { left: 111px; }
  .price--payout { left: 323px; }
  .price--shelter { left: 651px; }
  .price span { display: block; }
  .about, .raffle {
    position: absolute;
    left: 51px;
    width: 800px;
    margin: 0;
    color: var(--white);
    font-size: 14px;
    line-height: 20px;
    letter-spacing: 0.5px;
  }
  .about { top: 846px; }
  .raffle { top: 1006px; }
  .lunch, .date, .venue {
    position: absolute;
    left: 0;
    width: 868px;
    margin: 0;
    text-align: center;
    color: var(--ink);
    font-weight: 400;
  }
  .lunch { top: 1084px; font-size: 24px; letter-spacing: 1.6px; }
  .date { top: 1123px; font-size: 22px; letter-spacing: 1.3px; }
  .venue { top: 1162px; font-size: 16.5px; letter-spacing: 1px; font-weight: 500; }
</style>
</head>
<body>
<main class="poster">
  <div class="hero-art" role="img" aria-label="Illustration of a happy black and white dog with its tongue out, standing in a green meadow under a blue sky with white clouds, framed by dark tree foliage"></div>

  <h1 class="event-title">Tossin' for Tails on Cinco De Mayo<br>Disc Golf Tournament</h1>

  <p class="format">Two Rounds: First round singles for cash prize,<br>followed by best-to-worst doubles for cash prize.</p>

  <p class="price price--entry"><span>$30</span><span>Entry</span></p>
  <p class="price price--payout"><span>$15</span><span>Payout</span></p>
  <p class="price price--shelter"><span>$15</span><span>Wag Haven Shelter</span></p>

  <p class="about">
    Wag Haven Shelter is a community outreach program and animal rescue.<br>
    We offer free and low cost spay/neuter, flea/tick meds, food, treats, toys,<br>
    collars and leashes to low income and<br>
    homeless families in the North San Juan area.<br>
    &nbsp;WHS also rescues senior and disabled animals from across the globe.<br>
    WHS offer a hospice care to many of the animals.<br>
    You can find more information on our website: www.waghaven-example.org
  </p>

  <p class="raffle">
    RAFFLE: We will have a donation bin set up at the event to collect new and gently used leashes,<br>
    collars, dog beds, puppy pads, male wraps, toys, jackets, towels, blankets,<br>
    brio laundry detergent and Vexol wipes, for every items donated you will receive one raffle ticket.
  </p>

  <p class="lunch">Cinco De Mayo themed lunch provided</p>
  <p class="date">May 5th, 2018 Check in at 9 am</p>
  <p class="venue">Hollis Green 317 Marlow Street Grass Valley, Ca</p>
</main>
</body>
</html>
```